Dovanne Luxury Landscapes

A landscape business card.

Target Market(s)

Middle aged and up. Professionals.

Industry/Entity Type

Landscape

Contact Information for Business Card

Waverley

Colors
0054AA
0677BA
7BADD7
CADEEF
E8F1F8
0094D4
00A9DD
6FCCEA
C7EBF8
E9F6FB

Requirements
Must have
• The color blue and silver be very attractive
Nice to have
• An embossed logo. A watermark of a plant or something that indicates that we are a landscape company in the background of the backside where list of services are offered. . List of services on the back.
Should not have
• Red, yellow, orange.

```html
<!DOCTYPE html>
<html lang="en">
<head>
<meta charset="utf-8">
<title>Dovanne Luxury Landscapes – Business Card</title>
<link rel="stylesheet" href="https://fonts.googleapis.com/css2?family=Open+Sans:wght@400;600;700&display=swap">
<style>
  :root {
    --stage: #e9ecf1;
    --card-blue: #2f37a8;
    --card-blue-deep: #262d94;
    --silver: #dde0ec;
    --ink-blue: #2b38a3;
    --ink-text: #2a2a33;
    --card-white: #ffffff;
    --rule: #3a46b0;
  }
  * { margin: 0; padding: 0; box-sizing: border-box; }
  html, body {
    width: 1200px; height: 900px; overflow: hidden;
    background: var(--stage);
    font-family: "Open Sans", sans-serif;
  }
  .stage {
    position: relative; width: 1200px; height: 900px;
    display: flex; flex-direction: column; align-items: center; justify-content: center; gap: 50px;
  }
  .card {
    position: relative; width: 595px; height: 340px; border-radius: 26px; overflow: hidden;
    box-shadow: 0 6px 18px rgba(20, 25, 60, 0.18);
  }

  /* Front side */
  .card-front { background: var(--card-blue); }
  .card-front .pattern-field {
    position: absolute; inset: 0;
    background: linear-gradient(135deg, #3840b0 0%, var(--card-blue) 45%, var(--card-blue-deep) 100%);
  }
  .card-front .brand {
    position: absolute; left: 0; right: 0; top: 50%; transform: translateY(-50%);
    text-align: center; color: var(--silver); font-weight: 600; text-transform: uppercase;
  }
  .brand .brand-name { display: block; font-size: 46px; letter-spacing: 3px; line-height: 1.1; }
  .brand .brand-tag { display: block; font-size: 21px; letter-spacing: 3px; margin-top: 4px; }

  /* Back side */
  .card-back { background: var(--card-white); }
  .contact-layout {
    position: absolute; inset: 0; display: flex; align-items: center; justify-content: center; gap: 26px;
  }
  .holder-name { color: var(--ink-blue); font-weight: 700; font-size: 30px; letter-spacing: -0.3px; }
  .divider { width: 1.5px; height: 104px; background: var(--rule); }
  .contact-list { list-style: none; color: var(--ink-text); font-size: 15px; line-height: 1.45; }
  .contact-list li { display: flex; align-items: center; gap: 7px; }
  .contact-list svg { width: 13px; height: 13px; fill: var(--ink-blue); flex: none; }
  .contact-list .address { display: block; margin-top: 6px; }
</style>
</head>
<body>
<main class="stage">
  <section class="card card-front" aria-label="Card front">
    <div class="pattern-field" role="img" aria-label="Tonal blue repeating monogram pattern background"></div>
    <h1 class="brand">
      <span class="brand-name">Dovanne</span>
      <span class="brand-tag">Luxury Landscapes</span>
    </h1>
  </section>

  <section class="card card-back" aria-label="Card back">
    <div class="contact-layout">
      <h2 class="holder-name">Marla Kettering</h2>
      <div class="divider"></div>
      <ul class="contact-list">
        <li>
          <svg viewBox="0 0 24 24" aria-hidden="true"><path d="M6.6 10.8a15.1 15.1 0 0 0 6.6 6.6l2.2-2.2a1 1 0 0 1 1-.25 11.4 11.4 0 0 0 3.6.57 1 1 0 0 1 1 1V20a1 1 0 0 1-1 1A17 17 0 0 1 3 4a1 1 0 0 1 1-1h3.5a1 1 0 0 1 1 1c0 1.25.2 2.45.57 3.57a1 1 0 0 1-.25 1z"/></svg>
          902-555-LAWN
        </li>
        <li>
          <svg viewBox="0 0 24 24" aria-hidden="true"><path d="M12 2a10 10 0 1 0 0 20 10 10 0 0 0 0-20zm6.9 6h-2.9a15.7 15.7 0 0 0-1.4-3.6A8 8 0 0 1 18.9 8zM12 4c.8 1.2 1.5 2.5 1.9 4h-3.8c.4-1.5 1.1-2.8 1.9-4zM4.3 14a8 8 0 0 1 0-4h3.4a16.5 16.5 0 0 0 0 4zm.8 2h2.9c.3 1.3.8 2.5 1.4 3.6A8 8 0 0 1 5.1 16zM8 8H5.1a8 8 0 0 1 4.3-3.6C8.8 5.5 8.3 6.7 8 8zm4 12c-.8-1.2-1.5-2.5-1.9-4h3.8c-.4 1.5-1.1 2.8-1.9 4zm2.3-6H9.7a14.7 14.7 0 0 1 0-4h4.6a14.7 14.7 0 0 1 0 4zm.3 5.6c.6-1.1 1.1-2.3 1.4-3.6h2.9a8 8 0 0 1-4.3 3.6zm1.7-5.6a16.5 16.5 0 0 0 0-4h3.4a8 8 0 0 1 0 4z"/></svg>
          www.dovanne.com
        </li>
        <li class="address">18B Birchmount Road, Waverley,<br>Nova Scotia, B2R 4K7</li>
      </ul>
    </div>
  </section>
</main>
</body>
</html>
```